Business card Zottelgarten

Business card is for a self-employed dog trainer with own dog school. Name and logo of the dog school are available. Color specifications as well. The design should be classy and minimalist, but also modern. An already existing idea would be: Front: Only the logo Back: Contact data

Font styles to use
Serif
Sans Serif
Other font styles liked:
• Trajan Pro

Colors
f78f20

Requirements
Must have
• Name: Margit Wendler-Rasch Title: Dipl. Dog Trainer Contain my logo Follow my font and color preferences (see files)

```html
<!DOCTYPE html>
<html lang="en">
<head>
<meta charset="utf-8">
<title>Zottelgarten – Business Card</title>
<link rel="stylesheet" href="https://fonts.googleapis.com/css2?family=Cinzel:wght@400;500&display=swap">
<style>
  :root {
    --page: #efefef;
    --card-white: #ffffff;
    --brand-orange: #f78f20;
    --brand-brown: #7b6859;
    --ink: #5f6270;
    --rule: #7f8595;
    --icon: #6b6f7c;
    --logo-white: #ffffff;
  }
  * { margin: 0; padding: 0; box-sizing: border-box; }
  html, body {
    width: 1200px; height: 1000px; overflow: hidden;
    background: var(--page);
  }
  .canvas { position: relative; width: 1200px; height: 1000px; }

  .card { position: absolute; overflow: hidden; }

  .card-front { left: 456px; top: 75px; width: 674px; height: 384px; background: var(--brand-orange); }
  .card-front svg { display: block; width: 100%; height: 100%; }
  .brand-name { font-family: "Cinzel", "Times New Roman", serif; font-weight: 400; }

  .card-back {
    left: 142px; top: 506px; width: 679px; height: 387px;
    background: var(--card-white);
    font-family: "Cinzel", "Times New Roman", serif;
    color: var(--ink);
  }
  .holder-name {
    position: absolute; left: 0; right: 0; top: 85px;
    text-align: center; font-size: 30px; font-weight: 400; letter-spacing: 0.5px; line-height: 1;
  }
  .holder-title {
    position: absolute; left: 0; right: 0; top: 124px;
    text-align: center; font-size: 16px; line-height: 1; letter-spacing: 0.3px;
  }
  .divider {
    position: absolute; left: 68px; width: 537px; top: 157px;
    height: 3px; background: var(--rule);
  }
  .contact-list { list-style: none; position: absolute; left: 188px; top: 183px; }
  .contact-item {
    display: flex; align-items: center; height: 37px;
    font-size: 19px; line-height: 1;
  }
  .contact-item svg { width: 16px; height: 16px; margin-right: 16px; fill: var(--icon); flex: none; }
</style>
</head>
<body>
<main class="canvas">

  <section class="card card-front" aria-label="Card front">
    <svg viewBox="0 0 842 480" preserveAspectRatio="none">
      <path class="brown-arc" fill="var(--brand-brown)"
            d="M0 0 H842 V146 C760 370 570 424 420 421 C250 418 80 330 0 131 Z"/>
      <path class="stitch-line" fill="none" stroke="#ffffff" stroke-width="3" stroke-dasharray="20 12"
            d="M4 84 C90 300 250 394 420 396 C590 398 760 330 840 92"/>
      <circle class="brand-disc" cx="425" cy="200" r="80" fill="var(--logo-white)"/>
      <text class="brand-name" x="425" y="322" text-anchor="middle" font-size="37"
            letter-spacing="2" fill="var(--logo-white)">ZOTTELGARTEN</text>
      <text class="brand-url" x="425" y="335" text-anchor="middle" font-size="9.5"
            font-family="Cinzel, serif" letter-spacing="6" fill="var(--logo-white)">WWW.ZOTTELGARTEN.CH</text>
    </svg>
  </section>

  <section class="card card-back" aria-label="Card back">
    <h1 class="holder-name">Margit Wendler-Rasch</h1>
    <p class="holder-title">Dipl. Dog Trainer</p>
    <div class="divider"></div>
    <ul class="contact-list">
      <li class="contact-item">
        <svg viewBox="0 0 16 16" aria-hidden="true"><path d="M8 1 L15 7.5 L13 7.5 L13 14 L9.8 14 L9.8 10 L6.2 10 L6.2 14 L3 14 L3 7.5 L1 7.5 Z"/></svg>
        <span>Your Adrs</span>
      </li>
      <li class="contact-item">
        <svg viewBox="0 0 16 16" aria-hidden="true"><path d="M3.6 1.2 L6 1 L7.2 4.6 L5.6 6 C6.4 7.8 8.2 9.6 10 10.4 L11.4 8.8 L15 10 L14.8 12.4 C14.6 13.8 13.4 15 12 15 C6.4 14.6 1.4 9.6 1 4 C1 2.6 2.2 1.4 3.6 1.2 Z"/></svg>
        <span>+113 123 456 789</span>
      </li>
      <li class="contact-item">
        <svg viewBox="0 0 16 16" aria-hidden="true"><path d="M1 3 H15 V4 L8 8.6 L1 4 Z M1 5.4 L8 10 L15 5.4 V13 H1 Z"/></svg>
        <span>company@email.com</span>
      </li>
      <li class="contact-item">
        <svg viewBox="0 0 16 16" aria-hidden="true"><path fill-rule="evenodd" d="M8 1 A7 7 0 1 1 8 15 A7 7 0 1 1 8 1 Z M8 2.4 C7.2 3.4 6.6 5 6.5 7.3 H9.5 C9.4 5 8.8 3.4 8 2.4 Z M6.5 8.7 C6.6 11 7.2 12.6 8 13.6 C8.8 12.6 9.4 11 9.5 8.7 Z M2.5 7.3 H5.1 C5.2 5.4 5.6 3.9 6.2 2.7 C4.2 3.3 2.8 5.1 2.5 7.3 Z M10.9 7.3 H13.5 C13.2 5.1 11.8 3.3 9.8 2.7 C10.4 3.9 10.8 5.4 10.9 7.3 Z M2.5 8.7 C2.8 10.9 4.2 12.7 6.2 13.3 C5.6 12.1 5.2 10.6 5.1 8.7 Z M10.9 8.7 C10.8 10.6 10.4 12.1 9.8 13.3 C11.8 12.7 13.2 10.9 13.5 8.7 Z"/></svg>
        <span>www.zcompanyname.com</span>
      </li>
    </ul>
  </section>

</main>
</body>
</html>
```